Banner for offer and invoice document showing benefits

We need a banner that we can include in our offers in the PDF document. The banner is intended to explain our so-called best price guarantee to the customer. The attached pictures show the current banner that we want to replace and the best price stamp that we want to include in the banner.

The authorized and dök badge should be part of the new banner.

Target Market(s)

DIY, B2C

```html
<!DOCTYPE html>
<html lang="de">
<head>
<meta charset="utf-8">
<title>BestPreisGarantie Banner</title>
<link rel="stylesheet" href="https://fonts.googleapis.com/css2?family=Alfa+Slab+One&display=swap">
<style>
  :root {
    --banner-red: #cc0000;
    --headline-white: #fbfbf7;
    --headline-yellow: #ffe300;
    --badge-silver: #d3d9e6;
    --badge-blue: #1d4596;
    --illustration-skin: #d9b89a;
    --illustration-sleeve: #7d7f86;
  }
  html, body {
    margin: 0;
    padding: 0;
    overflow: hidden;
  }
  body {
    width: 1200px;
    height: 240px;
  }
  .banner {
    position: relative;
    width: 1200px;
    height: 240px;
    background: var(--banner-red);
    overflow: hidden;
  }
  .thumbs-illustration {
    position: absolute;
    left: 13px;
    top: 112px;
    width: 122px;
    height: 128px;
    border-radius: 40px 40px 0 0;
    background: linear-gradient(180deg, var(--illustration-skin) 0%, var(--illustration-skin) 45%, var(--illustration-sleeve) 100%);
  }
  .headline {
    position: absolute;
    left: 102px;
    top: 77px;
    margin: 0;
    font-family: "Alfa Slab One", "Rockwell", serif;
    font-weight: 400;
    font-size: 74px;
    line-height: 1;
    letter-spacing: 0.5px;
    color: var(--headline-white);
    white-space: nowrap;
  }
  .headline .accent {
    color: var(--headline-yellow);
  }
  .badges {
    position: absolute;
    left: 870px;
    top: 30px;
    width: 300px;
    height: 180px;
  }
</style>
</head>
<body>
  <div class="banner">
    <div class="thumbs-illustration" role="img" aria-label="Illustration: drei Hände mit erhobenem Daumen"></div>

    <h1 class="headline">Best<span class="accent">Preis</span>Garantie</h1>

    <svg class="badges" viewBox="0 0 300 180" role="img" aria-label="Platzhalter für Dök-Siegel und Partner-Abzeichen">
      <circle class="certificate-badge" cx="86" cy="88" r="82" fill="var(--badge-silver)"/>
      <circle class="partner-badge" cx="233" cy="95" r="57" fill="var(--badge-blue)"/>
    </svg>
  </div>
</body>
</html>
```